Retail Sign for Houseplant Campaign

Sign will measure 3 to 4 foot tall by 22.2inches and place on rolling racks of houseplants for a retail promotion in The Brickfield Yard. The theme of the promotion will be "New Year, New You!" Selling points which should be on the sign are Houseplants give you a taste of nature, Houseplants boost air quality inside your home, Indoor plants reduce anxiety, Indoor plants make you more productive, Houseplants improve your concentration and memory.
Updates

Target Market(s)

People who love plants

Industry/Entity Type

Horticulture/ retail

Colors
00AB8E
00BBA5
67D7C9
C6EFE9
E9F9F6
59FF00
82FF00
B8FF75
E3FFCB
F4FFEA
FFF300
FFF600
FEFA6F
FFFEC7
FFFEE8

Requirements
Must have
• Must feel energetic and encourage people to buy plants. Should include 1-2 photos and the selling points listed

```html
<!DOCTYPE html>
<html lang="en">
<head>
<meta charset="utf-8">
<title>Houseplants – New Year, New You!</title>
<link rel="stylesheet" href="https://fonts.googleapis.com/css2?family=Open+Sans:wght@500&family=Archivo+Black&family=Kaushan+Script&family=Montserrat:wght@500&display=swap">
<style>
  :root {
    --paper: #ffffff;
    --brand-green: #3f5a22;
    --olive: #6e6431;
    --olive-deep: #4d4420;
    --olive-dark: #3d361a;
    --gold: #f3b90c;
    --sun: #fff300;
    --lime-text: #2c4a17;
    --white: #ffffff;
  }
  * { margin: 0; padding: 0; box-sizing: border-box; }
  html, body { width: 741px; height: 1200px; overflow: hidden; background: var(--paper); }
  .sign {
    position: relative;
    width: 741px;
    height: 1200px;
    overflow: hidden;
    background: linear-gradient(180deg, var(--olive) 0%, var(--olive-deep) 100%);
  }
  .brand-header {
    position: absolute; left: 0; top: 0; width: 741px; height: 185px;
    background: var(--paper);
    display: flex; align-items: center; padding-left: 30px; gap: 26px;
  }
  .brand-mark { width: 130px; height: 130px; background: var(--brand-green); flex: none; }
  .brand-name {
    font-family: "Montserrat", sans-serif; font-weight: 500; color: var(--brand-green);
    line-height: 1;
  }
  .brand-name .line-1 { display: block; font-size: 92px; letter-spacing: 1px; }
  .brand-name .line-2 { display: block; font-size: 36px; letter-spacing: 26px; margin-top: 6px; padding-left: 4px; }

  .headline {
    position: absolute; left: 34px; top: 228px;
    font-family: "Archivo Black", sans-serif; font-size: 78px; color: var(--gold);
    letter-spacing: 2px; line-height: 1;
  }
  .benefits { position: absolute; left: 0; top: 328px; width: 741px; list-style: none; }
  .benefits li {
    height: 53px;
    font-family: "Open Sans", sans-serif; font-weight: 500; font-size: 41px;
    color: var(--white); line-height: 51px; padding-left: 26px; white-space: nowrap;
    background: linear-gradient(180deg, rgba(0,0,0,0.18), rgba(0,0,0,0.05));
    border-top: 2px solid rgba(255,255,255,0.14);
  }
  .benefits .indent { padding-left: 270px; }
  .benefits .indent-sm { padding-left: 56px; }

  .lifestyle-photo {
    position: absolute; left: 0; top: 702px; width: 741px; height: 498px;
    background: linear-gradient(160deg, #d8d4c8 0%, #b9b6a4 35%, #7f8f5a 70%, #556a34 100%);
  }
  .sun-wave { position: absolute; left: 0; top: 700px; width: 741px; height: 500px; }
  .sign-off {
    position: absolute; right: 18px; bottom: 24px; text-align: right;
  }
  .sign-off .top {
    display: block; font-family: "Archivo Black", sans-serif; font-size: 50px;
    color: var(--lime-text); line-height: 1;
  }
  .sign-off .bottom {
    display: block; font-family: "Kaushan Script", cursive; font-size: 52px;
    color: var(--white); line-height: 1.1; margin-right: 12px;
  }
</style>
</head>
<body>
<main class="sign">
  <header class="brand-header">
    <div class="brand-mark"></div>
    <div class="brand-name"><span class="line-1">VERDANT</span><span class="line-2">HOLLOW</span></div>
  </header>

  <h1 class="headline">HOUSEPLANTS</h1>
  <ul class="benefits">
    <li>-give you a taste of nature,</li>
    <li>-boost air quality</li>
    <li class="indent">inside your home,</li>
    <li>-reduce anxiety,</li>
    <li>-make you more productive,</li>
    <li>-improve your</li>
    <li class="indent-sm">concentration and memory.</li>
  </ul>

  <div class="lifestyle-photo" role="img" aria-label="Photo of a relaxed woman resting on a white sofa in a bright living room surrounded by potted houseplants"></div>

  <svg class="sun-wave" viewBox="0 0 741 500" aria-hidden="true">
    <defs>
      <linearGradient id="sunFill" x1="0" y1="0" x2="0" y2="1">
        <stop offset="0" stop-color="#fefa6f"/>
        <stop offset="0.6" stop-color="#f3c40c"/>
        <stop offset="1" stop-color="#c7960a"/>
      </linearGradient>
    </defs>
    <path d="M600 0 C560 90 640 170 600 250 C575 300 660 320 741 310 L741 0 Z" fill="url(#sunFill)" opacity="0.85"/>
    <path d="M0 410 C150 370 300 410 420 400 C540 390 620 330 741 320 L741 500 L0 500 Z" fill="url(#sunFill)"/>
    <path d="M0 440 C160 420 330 460 500 440 C600 430 680 405 741 400 L741 500 L0 500 Z" fill="var(--olive-dark)"/>
    <g stroke="var(--sun)" stroke-width="6" stroke-linecap="round">
      <line x1="40" y1="425" x2="200" y2="425"/>
      <line x1="40" y1="445" x2="180" y2="445"/>
      <line x1="40" y1="465" x2="160" y2="465"/>
    </g>
  </svg>

  <p class="sign-off"><span class="top">NEW YEAR,</span><span class="bottom">New You!</span></p>
</main>
</body>
</html>
```